Marlow Crest Group (Real Estate and Investment)

A high end, clean design.
We are a real estate company with sales, asset management and investment divisions. We want to use a black and white scheme which is really high end feel. The back of the card can just be the logo (black background with the white writing) as we will probably emboss this when we print)

Target Market(s)

High level investors, high end houses for sale

Industry/Entity Type

Business

Contact Information for Business Card

Name, position, phone number and email address
Glen Varley, Managing Director, 0437259064 and glen@marlowcrest-example.com.au

Requirements
Must have
• Back of the card to be the black background with the white writing (as per the attached images). Would like the capacity to emboss the writing and logo

```html
<!DOCTYPE html>
<html lang="en">
<head>
<meta charset="utf-8">
<title>Marlow Crest Group – Glen Varley</title>
<link rel="stylesheet" href="https://fonts.googleapis.com/css2?family=Jura:wght@400;500;600&display=swap">
<style>
  :root {
    --card-dark: #1c1c1c;
    --card-mid: #252525;
    --card-light: #2d2d2d;
    --ink: #ffffff;
    --ink-soft: #f2f2f2;
  }
  * { margin: 0; padding: 0; box-sizing: border-box; }
  html, body {
    width: 1200px;
    height: 702px;
    overflow: hidden;
    background: var(--card-dark);
  }
  .card {
    position: relative;
    width: 1200px;
    height: 702px;
    overflow: hidden;
    font-family: "Jura", sans-serif;
    color: var(--ink);
  }
  .card__texture {
    position: absolute;
    inset: 0;
    background:
      radial-gradient(ellipse at 30% 40%, var(--card-light) 0%, transparent 60%),
      linear-gradient(160deg, var(--card-mid) 0%, var(--card-dark) 55%, var(--card-mid) 100%);
  }
  .card__divider {
    position: absolute;
    left: 0;
    top: 0;
  }
  .brand {
    position: absolute;
    left: 60px;
    width: 472px;
    top: 212px;
    display: flex;
    flex-direction: column;
    align-items: center;
  }
  .brand__ring {
    width: 174px;
    height: 174px;
    border: 2px solid var(--ink);
    border-radius: 50%;
  }
  .brand__name {
    margin-top: 44px;
    font-size: 34px;
    font-weight: 500;
    letter-spacing: 0.5px;
    text-transform: uppercase;
    white-space: nowrap;
  }
  .contact {
    position: absolute;
    left: 680px;
    top: 266px;
  }
  .contact__name {
    font-size: 44px;
    font-weight: 600;
    line-height: 58px;
    letter-spacing: 4px;
    text-transform: uppercase;
    white-space: nowrap;
  }
  .contact__initial {
    font-size: 62px;
  }
  .contact__gap {
    display: inline-block;
    width: 18px;
  }
  .contact__role,
  .contact__phone,
  .contact__email {
    font-size: 25px;
    font-weight: 500;
    line-height: 33px;
    letter-spacing: 0.5px;
    color: var(--ink-soft);
    white-space: nowrap;
  }
</style>
</head>
<body>
  <main class="card">
    <div class="card__texture" role="img" aria-label="Dark charcoal geometric triangle texture across the card"></div>

    <svg class="card__divider" width="1200" height="702" viewBox="0 0 1200 702" aria-hidden="true">
      <line x1="599" y1="69" x2="594" y2="629" stroke="#ffffff" stroke-width="3"/>
    </svg>

    <section class="brand">
      <div class="brand__ring" aria-hidden="true"></div>
      <p class="brand__name">Marlow Crest Group</p>
    </section>

    <section class="contact">
      <h1 class="contact__name"><span class="contact__initial">G</span>len<span class="contact__gap"></span><span class="contact__initial">V</span>arley</h1>
      <p class="contact__role">Managing Director</p>
      <p class="contact__phone">0437259064</p>
      <p class="contact__email">glen@marlowcrest-example.com.au</p>
    </section>
  </main>
</body>
</html>
```